Creative label for amber glass candle jar.

We are a candle company. Our products are handmade by us and natural. We are looking for something minimalistic and unique. We need a label for our candle jars (amber glass with black lid). Our current label doesn't match these requirements. We would like our products to be stocked in London shop, therefore design has to be up to a high standard. Jar specification Diameter (mm) 65 Height without cap (mm) 80. We want the new design to be different from the current one. It's just a guide for wording.
We should be able adjust the label, to change scent name.
Our scents are
*Coconut & Vanilla
*Lavender
*Bergamot
*Italian Garden
*Hygge
*Eucalyptus & Peppermint
*Coffee
*Cedarwood & Juniperberry
To know more about us, visit our website www.wrenfieldcandles.com or instagram.com/wrenfieldcandles
Good luck!
Industry/Entity Type
It Company
Colors
Designer to choose colors to be used in the design.
Requirements
Must have
- * I have attached two of our logos, label design must include one of them.
- *has to mention that it's made in London
- *has to say that candle is natural/made with essential oils
- *has to have scent name and No. on it..
- Label can be vertical or horizontal, but has to be square/rectangular,.
Should not have
- Label should not be round

```html
<!DOCTYPE html>
<html lang="en">
<head>
<meta charset="UTF-8">
<title>Wrenfield — Bergamot Candle Label</title>
<link rel="stylesheet" href="https://fonts.googleapis.com/css2?family=Marcellus&family=Jost:wght@400&display=swap">
<style>
  :root {
    --page-bg: #f7f7f6;
    --label-light: #ece1cc;
    --label-mid: #e3d6bd;
    --label-dark: #d3c5ab;
    --ink: #1b1816;
  }
  * { margin: 0; padding: 0; box-sizing: border-box; }
  html, body {
    width: 1200px;
    height: 1098px;
    overflow: hidden;
    background: var(--page-bg);
  }
  .canvas {
    position: relative;
    width: 1200px;
    height: 1098px;
  }
  .label {
    position: absolute;
    left: 145px;
    top: 154px;
    width: 910px;
    height: 790px;
    background: linear-gradient(90deg, var(--label-dark) 0%, var(--label-light) 30%, var(--label-mid) 65%, var(--label-dark) 100%);
    color: var(--ink);
    text-align: center;
  }
  .brand-mark {
    position: absolute;
    top: 110px;
    left: 0;
    right: 0;
    display: flex;
    justify-content: center;
    align-items: center;
    gap: 22px;
    font-family: "Jost", sans-serif;
    font-weight: 400;
    font-size: 58px;
    letter-spacing: 0.22em;
    line-height: 1;
  }
  .brand-mark .brand-dot {
    width: 26px;
    height: 26px;
    background: var(--ink);
  }
  .scent-name {
    position: absolute;
    top: 395px;
    left: 0;
    right: 0;
    font-family: "Marcellus", serif;
    font-size: 104px;
    line-height: 1;
    letter-spacing: 0.02em;
  }
  .details {
    position: absolute;
    top: 518px;
    left: 0;
    right: 0;
    font-family: "Jost", sans-serif;
    font-size: 26px;
    line-height: 48px;
  }
  .details .wax {
    display: inline-block;
    padding: 0 22px;
    border-bottom: 2px solid var(--ink);
    line-height: 40px;
    margin-bottom: 4px;
  }
  .details p { margin: 0; }
  .origin {
    position: absolute;
    top: 684px;
    left: 0;
    right: 0;
    font-family: "Jost", sans-serif;
    font-size: 28px;
    letter-spacing: 0.12em;
  }
</style>
</head>
<body>
  <main class="canvas">
    <section class="label">
      <div class="brand-mark">
        <span class="brand-dot"></span>
        <span class="brand-name">WRENFIELD</span>
      </div>
      <h1 class="scent-name">BERGAMOT</h1>
      <div class="details">
        <span class="wax">100% SOY WAX</span>
        <p class="natural">MADE WITH ESSENTIAL OILS</p>
        <p class="batch-number">No......</p>
      </div>
      <p class="origin">MADE IN LONDON</p>
    </section>
  </main>
</body>
</html>
```